Need a solid log.
My company Sales: OrbiCast, Halcyon Beam, Vorlan Internet
Design and installation of WI_FI systems.
Fulfillment company for installations in the Electronics industry

Industry/Entity Type

Electronics

Contact Information for Business Card

Peter R. Hollowell
President
Phone: 479.555.0182 Cell: 479.5550947 prhollowell@brightharbornet.biz
Bright Harbor Networks
Pinebrook, AL. 35990

```html
<!DOCTYPE html>
<html lang="en">
<head>
<meta charset="utf-8">
<title>Bright Harbor Networks — Business Card</title>
<link rel="stylesheet" href="https://fonts.googleapis.com/css2?family=Gelasio:wght@400;500;600;700&display=swap">
<style>
  :root {
    --backdrop: #6b3a1f;
    --card-white: #ffffff;
    --brand-blue: #0a74cc;
    --ink: #111111;
    --ink-soft: #5a5a5a;
    --rule: #333333;
  }
  * { margin: 0; padding: 0; box-sizing: border-box; }
  html, body {
    width: 1200px;
    height: 900px;
    overflow: hidden;
    background: var(--backdrop);
  }
  .stage {
    position: relative;
    width: 1200px;
    height: 900px;
  }
  .business-card {
    position: absolute;
    left: 291px;
    top: 269px;
    width: 618px;
    height: 362px;
    background: var(--card-white);
    transform: scale(1.7);
    transform-origin: center center;
    font-family: "Gelasio", Georgia, serif;
    color: var(--ink);
  }
  .brand-band {
    position: absolute;
    left: 0; top: 0;
    width: 100%;
    height: 91px;
    background: var(--brand-blue);
    display: flex;
    align-items: center;
    justify-content: center;
  }
  .brand-name {
    color: var(--card-white);
    font-weight: 700;
    font-size: 30px;
    font-variant: small-caps;
    letter-spacing: 0.5px;
    word-spacing: 6px;
    line-height: 1;
    padding-top: 4px;
  }
  .services {
    position: absolute;
    left: 0;
    top: 97px;
    width: 322px;
    text-align: right;
    font-size: 14.5px;
    line-height: 21px;
  }
  .services .sep { margin: 0 5px; }
  .divider {
    position: absolute;
    left: 330px;
    top: 97px;
    width: 1px;
    height: 42px;
    background: var(--rule);
  }
  .tagline {
    position: absolute;
    left: 338px;
    top: 99px;
    width: 270px;
    font-size: 14px;
    line-height: 18px;
    color: var(--ink-soft);
  }
  .person {
    position: absolute;
    left: 0;
    top: 235px;
    width: 100%;
    text-align: center;
  }
  .person-name {
    font-size: 20px;
    line-height: 24px;
    font-weight: 400;
  }
  .person-title {
    font-size: 16.5px;
    line-height: 22px;
    font-weight: 600;
    letter-spacing: 0.3px;
  }
  .contact-rule {
    position: absolute;
    left: 26px;
    top: 294px;
    width: 567px;
    height: 1px;
    background: var(--rule);
  }
  .contact {
    position: absolute;
    left: 0;
    top: 303px;
    width: 100%;
    text-align: center;
    font-size: 15px;
    line-height: 22px;
    font-weight: 600;
  }
  .contact .slash { margin: 0 8px; font-weight: 400; }
</style>
</head>
<body>
<main class="stage">
  <article class="business-card">
    <header class="brand-band">
      <h1 class="brand-name">Bright Harbor Networks</h1>
    </header>

    <p class="services">
      OrbiCast<span class="sep">|</span>Halcyon Beam<span class="sep">|</span>Vorlan Internet<br>
      Design and Installation of WIFI systems
    </p>
    <div class="divider"></div>
    <p class="tagline">Fulfillment company for installations<br>in the Electronics Industry</p>

    <section class="person">
      <p class="person-name">Peter R. Hollowell</p>
      <p class="person-title">President</p>
    </section>

    <div class="contact-rule"></div>
    <address class="contact" style="font-style: normal;">
      Pinebrook, AL. 35990<span class="slash">/</span>Phone: 479.555.0182<span class="slash">/</span>Cell: 479.5550947<br>
      Email: prhollowell@brightharbornet.biz
    </address>
  </article>
</main>
</body>
</html>
```